Quorzo Landing Page & Logo

We are building a landing page for a new blockchain-based project called Quorzo. The site should look modern and minimalistic with a very brief description of the upcoming project ("Unlock your Belmitra governance stack. Win weekly prizes and a quarterly jackpot!"), a viper logo (the animal - but can just be lettering) , and a button to subscribe for updates and early access.
Examples of similar pages:
https://pellow.finance/
https://www.trunemo.org/
https://merbisket.com/
https://k7.io/
https://www.drinnet.finance/
Target Market(s)
Crypto Users (Specifically Belmitra holders)
Coding
Coded - Design and coding required
Number of Pages Required
1 page
Look and feel
Each slider illustrates characteristics of the customer's brand and the style your logo design should communicate.

```html
<!DOCTYPE html>
<html lang="en">
<head>
<meta charset="utf-8">
<title>Quorzo — Belmitra Governance Prizes</title>
<link rel="stylesheet" href="https://fonts.googleapis.com/css2?family=Barlow+Condensed:wght@600;700&family=Poppins:wght@400&display=swap">
<style>
  :root {
    --bg-deep: #02020c;
    --bg-navy: #0a0a4a;
    --bg-blue: #10119a;
    --white: #ffffff;
    --accent-green: #19ef7c;
    --social-green: #17c96a;
    --button-blue: #04a3e0;
    --placeholder: #4a4a4a;
  }
  * { margin: 0; padding: 0; box-sizing: border-box; }
  html, body { width: 1200px; height: 542px; overflow: hidden; background: var(--bg-deep); }
  .page {
    position: relative;
    width: 1200px;
    height: 542px;
    overflow: hidden;
    font-family: "Poppins", sans-serif;
    color: var(--white);
  }
  .backdrop {
    position: absolute;
    inset: 0;
    background:
      radial-gradient(ellipse 520px 380px at 930px 330px, rgba(22, 24, 170, 0.75), transparent 70%),
      radial-gradient(ellipse 700px 260px at 300px 420px, rgba(20, 20, 120, 0.55), transparent 75%),
      linear-gradient(180deg, #03030f 0%, var(--bg-navy) 55%, #0c0c5a 88%, var(--bg-deep) 90%, #050520 100%);
  }
  .site-header {
    position: absolute;
    top: 32px;
    left: 141px;
    right: 141px;
    height: 44px;
    display: flex;
    align-items: center;
    justify-content: space-between;
  }
  .brand {
    font-family: "Barlow Condensed", sans-serif;
    font-weight: 700;
    font-size: 42px;
    line-height: 1;
    color: var(--white);
    letter-spacing: 0.5px;
  }
  .social-links { display: flex; gap: 7px; margin-top: -2px; }
  .social-link {
    width: 29px;
    height: 29px;
    border-radius: 50%;
    background: var(--social-green);
    display: block;
  }
  .hero { position: absolute; left: 142px; top: 163px; }
  .hero-title {
    font-family: "Barlow Condensed", sans-serif;
    font-weight: 700;
    font-size: 30px;
    line-height: 37px;
    text-transform: uppercase;
    letter-spacing: 0.2px;
  }
  .hero-title .highlight { color: var(--accent-green); }
  .hero-subtitle { margin-top: 14px; font-size: 13px; line-height: 18px; }
  .subscribe-form { margin-top: 14px; }
  .email-field {
    width: 357px;
    height: 42px;
    border: none;
    border-radius: 21px;
    background: var(--white);
    padding: 0 22px;
    font-family: "Poppins", sans-serif;
    font-size: 12px;
    color: var(--placeholder);
    display: block;
    margin-left: -1px;
  }
  .email-field::placeholder { color: var(--placeholder); }
  .subscribe-button {
    margin-top: 15px;
    margin-left: -1px;
    width: 151px;
    height: 42px;
    border: none;
    border-radius: 21px;
    background: var(--button-blue);
    color: var(--white);
    font-family: "Barlow Condensed", sans-serif;
    font-weight: 700;
    font-size: 19px;
    display: flex;
    align-items: center;
    justify-content: center;
    gap: 7px;
  }
  .site-footer {
    position: absolute;
    left: 141px;
    top: 507px;
    font-size: 13px;
  }
</style>
</head>
<body>
<main class="page">
  <div class="backdrop" role="img" aria-label="Dark navy backdrop with a faint network mesh and floating blue cubes"></div>

  <header class="site-header">
    <div class="brand">Quorzo</div>
    <nav class="social-links" aria-label="Social links">
      <a class="social-link" href="#" aria-label="Social profile one"></a>
      <a class="social-link" href="#" aria-label="Community chat"></a>
      <a class="social-link" href="#" aria-label="Photo profile"></a>
    </nav>
  </header>

  <section class="hero">
    <h1 class="hero-title">
      Unlock your Belmitra governance<br>
      stack. Win <span class="highlight">weekly prizes</span> and a<br>
      <span class="highlight">quarterly jackpot!</span>
    </h1>
    <p class="hero-subtitle">Subscribe For Updates And Early Access</p>
    <form class="subscribe-form">
      <input class="email-field" type="email" placeholder="Email Address" aria-label="Email Address">
      <button class="subscribe-button" type="button">
        SUBSCRIBE
        <svg width="21" height="21" viewBox="0 0 21 21" aria-hidden="true">
          <circle cx="10.5" cy="10.5" r="9.5" fill="none" stroke="#fff" stroke-width="1.4"/>
          <path d="M9 6.5 L13 10.5 L9 14.5" fill="none" stroke="#fff" stroke-width="1.6" stroke-linecap="round" stroke-linejoin="round"/>
        </svg>
      </button>
    </form>
  </section>

  <footer class="site-footer">Copyright 2022 Quorzo. All rights reserved.</footer>
</main>
</body>
</html>
```